OrchardLane Kiosk Signage

OrchardLane sell fresh fruit and vegetables online and from road side Kiosks.

We need to adapt the current logo for use as signs that will be displayed on roadside kiosks, please see the attached images to view and understand what the Kiosks look like.
The sign needs to:

1. Capture the attention of drivers and
2. Invite them to stop and purchase fresh fruit and veg
3. Communicate the URL www.OrchardLaneHarvest.co.nz
4. Communicate the OrchardLane brand
5. Use current logos and imagery

Solution

The designs must closely reflect the current OrchardLane logo (see files attached) and need to include the website. www.OrchardLaneHarvest.co.nz The colour palleted also needs to closely resemble the website.

The designs will be used for laser printed signage on vinyl for two applications

1. Kiosk front width: 2.400m x height: 1.000m (94 inches x 40 inches)
2. Kiosk sides: width 0.400m x height: 1.000m (15 inches x 40 inches)

The region where the kiosk's will display is large open space, green hills and fresh fruit and veg growers (orchards and farms everywhere). The region is well known for horticulture, agriculture, viticulture and farming.

Updates

Please note, the OrchardLane kiosk signage brief has been updated. (sorry for the inconvenience, but I think we uploaded an unfinished brief) 

We look forward to your submissions. 

Cheers, OrchardLane 

Target Market(s)

Passers buy - mainly in cars as the signage will be displayed on road side fruit and veg stalls. So the signage will be viewed by the general public, and capture those that are interested in purchasing fresh fruit and veg (direct from the farm or orchard)

Industry/Entity Type

Agriculture

Requirements
Must have
• Must match current logo and reflect the design aspects of the website www.orchardlaneharvest.co.nz
Needs to clearly communicate whats for sale, value and fresh produce
Nice to have
• It would be nice to make the tree component of the logo a feature.

```html
<!DOCTYPE html>
<html lang="en">
<head>
<meta charset="utf-8">
<title>OrchardLane Kiosk Side Sign</title>
<link rel="stylesheet" href="https://fonts.googleapis.com/css2?family=Alfa+Slab+One&family=Amatic+SC:wght@700&family=Zilla+Slab:wght@600&display=swap">
<style>
  :root {
    --kraft: #efe2c6;
    --kraft-deep: #e4d4b2;
    --leaf: #628a4f;
    --leaf-soft: #86a872;
  }
  html, body {
    margin: 0;
    padding: 0;
    width: 1200px;
    height: 3000px;
    overflow: hidden;
    background: var(--kraft);
  }
  .sign {
    display: block;
    width: 1200px;
    height: 3000px;
    background: var(--kraft);
  }
  .hand { font-family: "Amatic SC", "Arial Narrow", sans-serif; font-weight: 700; fill: var(--leaf); }
  .slab { font-family: "Alfa Slab One", "Rockwell", serif; fill: var(--leaf); }
  .tagline { font-family: "Zilla Slab", "Rockwell", serif; font-weight: 600; fill: var(--leaf); letter-spacing: 10px; }
  .brand-name { font-family: "Alfa Slab One", "Rockwell", serif; fill: var(--kraft); }
  .rule { stroke: var(--leaf); stroke-width: 10; }
  .flourish { fill: none; stroke: var(--leaf); stroke-width: 12; stroke-linecap: round; }
  .corner-foliage { fill: var(--leaf-soft); opacity: 0.75; }
  .brand-panel { fill: var(--leaf); }
  .social-tile { fill: none; stroke: var(--leaf); stroke-width: 10; }
</style>
</head>
<body>
<svg class="sign" viewBox="0 0 1200 3000" xmlns="http://www.w3.org/2000/svg">

  <!-- corner foliage -->
  <path class="corner-foliage" role="img" aria-label="Leafy foliage sprig in the top left corner" d="M0 0 H150 Q90 60 0 150 Z"/>
  <path class="corner-foliage" role="img" aria-label="Leafy foliage sprig in the top right corner" d="M1200 0 H1050 Q1110 60 1200 150 Z"/>
  <path class="corner-foliage" role="img" aria-label="Leafy foliage sprig in the bottom left corner" d="M0 3000 H150 Q90 2940 0 2850 Z"/>
  <path class="corner-foliage" role="img" aria-label="Leafy foliage sprig in the bottom right corner" d="M1200 3000 H1050 Q1110 2940 1200 2850 Z"/>

  <!-- header -->
  <g class="header">
    <text class="hand" x="600" y="145" font-size="118" text-anchor="middle" letter-spacing="2">FROM THE FARM</text>
    <text class="hand" x="600" y="272" font-size="118" text-anchor="middle" letter-spacing="2">TO YOUR TABLE</text>
    <path class="flourish" d="M60 240 Q90 200 130 225 Q175 255 215 225 Q245 205 275 225"/>
    <path class="flourish" d="M925 225 Q955 205 985 225 Q1025 255 1070 225 Q1110 200 1140 240"/>
  </g>

  <line class="rule" x1="55" y1="375" x2="1145" y2="375"/>

  <!-- headline -->
  <g class="headline">
    <text class="slab" x="55" y="532" font-size="107" textLength="1085" lengthAdjust="spacingAndGlyphs">COME AND SHOP AT</text>
    <text class="slab" x="55" y="707" font-size="217" textLength="1085" lengthAdjust="spacingAndGlyphs">THE BEST</text>
    <text class="slab" x="55" y="912" font-size="250" textLength="1090" lengthAdjust="spacingAndGlyphs">PLACE</text>
    <text class="slab" x="55" y="1070" font-size="171" textLength="1085" lengthAdjust="spacingAndGlyphs">TO GO FOR</text>
    <text class="slab" x="55" y="1282" font-size="243" textLength="1090" lengthAdjust="spacingAndGlyphs">FRESH,</text>
    <text class="slab" x="55" y="1487" font-size="250" textLength="1058" lengthAdjust="spacingAndGlyphs">FRUIT</text>
    <text class="slab" x="55" y="1682" font-size="225" textLength="1090" lengthAdjust="spacingAndGlyphs">AND VEG!</text>
  </g>

  <line class="rule" x1="55" y1="1762" x2="1145" y2="1762"/>

  <!-- brand block -->
  <g class="brand">
    <rect class="brand-panel" x="55" y="1832" width="1090" height="388" rx="40"/>
    <text class="brand-name" x="100" y="2005" font-size="170" textLength="1000" lengthAdjust="spacingAndGlyphs">ORCHARD</text>
    <text class="brand-name" x="100" y="2175" font-size="170" textLength="560" lengthAdjust="spacingAndGlyphs">LANE</text>
    <text class="tagline" x="55" y="2322" font-size="80" textLength="1090" lengthAdjust="spacingAndGlyphs">PRODUCE DELIVERED</text>
  </g>

  <line class="rule" x1="55" y1="2408" x2="1145" y2="2408"/>

  <!-- online -->
  <g class="online">
    <text class="hand" x="145" y="2580" font-size="125" textLength="530" lengthAdjust="spacingAndGlyphs">FIND US ONLINE!</text>
    <rect class="social-tile" x="742" y="2478" width="108" height="108" rx="14"/>
    <rect class="social-tile" x="917" y="2478" width="108" height="108" rx="14"/>
    <text class="slab" x="600" y="2728" font-size="86" text-anchor="middle" textLength="895" lengthAdjust="spacingAndGlyphs">/orchardlaneharvest</text>
    <text class="slab" x="600" y="2880" font-size="62" text-anchor="middle" textLength="1050" lengthAdjust="spacingAndGlyphs">www.OrchardLaneHarvest.co.nz</text>
  </g>
</svg>
</body>
</html>
```